Candle Box & Belly Band Design

Design Candle Box for Soy Candles along with a belly band design that can be used on off the shelf coloured boxes. It is for a premium brand of candle - so i want the packaging to reflect this. I have included must haves below.

The candle boxes will be a few different sizes, but for the purpose of the design it would be something like a cube 12 x 12 x 12 cms

The belly band for standard boxes to be something like 5cm wide on a 12 x 12 x 12cms cube box that goes all the way around the top to the bottom - holding the lid on and providing all the relevant information. Example of box with belly band uploaded

Our company Name : Hazel & Pip - our logo is uploaded

Target Market(s)

Premium Candle Buyers

Colors

Designer to choose colors to be used in the design.

Requirements
Must have
• Must have our logo - our logo can be in any colour
• Must state:
• Soy Candle, Hand Poured, Made in Melbourne,
• A space for the fragrance, size and burn time.
• For this project use Lime, Coconut & Elderfllower, 300grams, 50 Hour burn Time

```html
<!DOCTYPE html>
<html lang="en">
<head>
<meta charset="utf-8">
<title>Hazel &amp; Pip — Candle Box &amp; Belly Band</title>
<link href="https://fonts.googleapis.com/css2?family=Alegreya:ital@0;1&display=swap" rel="stylesheet">
<style>
  :root {
    --peach: #fde4da;
    --blush: #f8c3c7;
    --coral: #f49b9e;
    --brand-pink: #f5bfc3;
    --ink: #6b6b6b;
    --rule: #8a8a8a;
    --paper: #ffffff;
  }
  html, body {
    margin: 0; padding: 0;
    width: 1200px; height: 1200px;
    overflow: hidden;
    background: var(--paper);
  }
  .artboard { position: relative; width: 1200px; height: 1200px; }
  .band { position: absolute; }
  .band--gradient { background: linear-gradient(to bottom, var(--peach), var(--blush)); }
  .band--coral { background: var(--coral); }

  .brand-vertical {
    position: absolute;
    left: 487px; top: 169px; height: 250px; width: 60px;
    writing-mode: vertical-rl;
    transform: rotate(180deg);
    font-family: "Alegreya", serif;
    font-size: 52px; line-height: 60px;
    color: var(--brand-pink);
    text-align: center;
    white-space: nowrap;
  }
  .brand-mark {
    position: absolute;
    border-radius: 50%;
    background: linear-gradient(to right, var(--peach), var(--blush));
  }
  .brand-mark--coral { background: var(--coral); }
  .brand-name {
    position: absolute;
    font-family: "Alegreya", serif;
    font-size: 12.5px; line-height: 14px;
    color: var(--brand-pink);
    white-space: nowrap;
  }
  .brand-name--coral { color: var(--coral); }

  .rule { position: absolute; height: 0; border-top: 1px solid var(--rule); }
  .details {
    position: absolute; margin: 0;
    font-family: "Alegreya", serif; font-style: italic;
    color: var(--ink); white-space: nowrap;
  }
  .details--large { font-size: 13.5px; line-height: 16.5px; }
  .details--small { font-size: 6px; line-height: 8.3px; }
  .sep { font-style: normal; font-size: 0.6em; vertical-align: 0.2em; padding: 0 0.25em; }
  .origin {
    position: absolute; margin: 0;
    font-family: "Alegreya", serif; font-style: italic;
    color: var(--ink); white-space: nowrap;
  }
</style>
</head>
<body>
<main class="artboard">

  <!-- Box wrap -->
  <section class="box-wrap">
    <div class="band band--gradient" style="left:271px;top:61px;width:193px;height:663px"></div>
    <div class="band band--gradient" style="left:741px;top:61px;width:193px;height:663px"></div>
    <div class="brand-vertical">Hazel &amp; Pip</div>
    <div class="brand-mark" style="left:645px;top:163px;width:64px;height:64px"></div>
    <div class="rule" style="left:487px;top:561px;width:127px"></div>
    <p class="details details--large" style="left:487px;top:576px">
      Lime, Coconut &amp; Elderflower<br>
      Soy candle<span class="sep">|</span>Hand poured<br>
      300grams<span class="sep">|</span>50 hour burn time
    </p>
    <p class="origin" style="left:487px;top:691px;font-size:11px">Made in Melbourne</p>
  </section>

  <!-- Belly band, gradient -->
  <section class="belly-band">
    <div class="band band--gradient" style="left:236px;top:771px;width:101px;height:346px"></div>
    <div class="band band--gradient" style="left:481px;top:771px;width:102px;height:346px"></div>
    <div class="brand-mark" style="left:358px;top:938px;width:40px;height:40px"></div>
    <div class="brand-name" style="left:348px;top:992px">Hazel &amp; Pip</div>
    <div class="rule" style="left:349px;top:1034px;width:67px"></div>
    <p class="details details--small" style="left:349px;top:1041px">
      Lime, Coconut &amp; Elderflower<br>
      Soy candle<span class="sep">|</span>Hand poured<br>
      300grams<span class="sep">|</span>50 hour burn time
    </p>
    <p class="origin" style="left:348px;top:1101px;font-size:5.5px">Made in Melbourne</p>
  </section>

  <!-- Belly band, coral -->
  <section class="belly-band">
    <div class="band band--coral" style="left:623px;top:771px;width:101px;height:346px"></div>
    <div class="band band--coral" style="left:869px;top:771px;width:101px;height:346px"></div>
    <div class="brand-mark brand-mark--coral" style="left:746px;top:938px;width:40px;height:40px"></div>
    <div class="brand-name brand-name--coral" style="left:736px;top:992px">Hazel &amp; Pip</div>
    <div class="rule" style="left:736px;top:1034px;width:67px"></div>
    <p class="details details--small" style="left:736px;top:1041px">
      Lime, Coconut &amp; Elderflower<br>
      Soy candle<span class="sep">|</span>Hand poured<br>
      300grams<span class="sep">|</span>50 hour burn time
    </p>
    <p class="origin" style="left:736px;top:1101px;font-size:5.5px">Made in Melbourne</p>
  </section>

</main>
</body>
</html>
```